Stationery Design Project

Company name - Harborline Med

Wellness Consulting and training company. Run as a medical centre.
Logo design created already.
Looking for simplistic, yet innovative look.
Logo colours are blue and orange, so looking for something along those lines.

1) Need letter head with logo

2) Pen design

3) Cup - Drinking

4) Envelope

5) Business card - Launched as a separate project

No website yet.

Reason: Need business card and stationary design completed in these 5 days

Target Market(s)

35 to 60
Trendy and new age

Industry/Entity Type

Training

Colors
f37122
0255a3

Requirements
Must have
• Colours - Blue and orange
Nice to have
• Not too gaudy, but simple and succinct.

```html
<!DOCTYPE html>
<html lang="en">
<head>
<meta charset="UTF-8">
<title>Harborline Med — Letterhead</title>
<link href="https://fonts.googleapis.com/css2?family=Didact+Gothic&display=swap" rel="stylesheet">
<style>
  :root {
    --backdrop: #dedede;
    --paper: #f6f6f6;
    --brand-blue: #0255a3;
    --brand-orange: #f37122;
    --ink-grey: #5e6166;
    --rule-grey: #c9c9c9;
    --icon-blue: #3c74ad;
  }
  * { margin: 0; padding: 0; box-sizing: border-box; }
  html, body {
    width: 1200px;
    height: 968px;
    overflow: hidden;
    background: var(--backdrop);
    font-family: "Didact Gothic", "Century Gothic", sans-serif;
  }
  .letterhead {
    position: absolute;
    left: 282px;
    top: 34px;
    width: 636px;
    height: 900px;
    background: var(--paper);
    box-shadow: 0 2px 10px rgba(0,0,0,0.12);
  }
  .brand {
    position: absolute;
    left: 52px;
    top: 56px;
    display: flex;
    align-items: center;
    gap: 8px;
  }
  .brand-name {
    font-size: 24px;
    color: var(--brand-blue);
    letter-spacing: -0.2px;
  }
  .brand-dot {
    width: 12px;
    height: 12px;
    border-radius: 50%;
    background: var(--brand-orange);
  }
  .contact-footer {
    position: absolute;
    left: 52px;
    bottom: 58px;
    display: flex;
    align-items: center;
    gap: 20px;
    font-size: 10.5px;
    color: var(--ink-grey);
    line-height: 1.6;
  }
  .contact-group { display: flex; flex-direction: column; }
  .contact-line { display: flex; align-items: center; gap: 7px; }
  .contact-icon { width: 10px; height: 10px; flex: none; }
  .contact-divider {
    width: 1px;
    height: 26px;
    background: var(--rule-grey);
  }
</style>
</head>
<body>
  <main class="letterhead">
    <header class="brand">
      <span class="brand-name">Harborline Med</span>
      <span class="brand-dot"></span>
    </header>

    <footer class="contact-footer">
      <div class="contact-group phone-numbers">
        <div class="contact-line">
          <svg class="contact-icon" viewBox="0 0 10 10"><circle cx="5" cy="5" r="4.5" fill="none" stroke="var(--icon-blue)" stroke-width="1"/><path d="M3.4 2.8 L4.3 2.6 L4.7 3.8 L4.1 4.3 Q4.6 5.4 5.7 5.9 L6.2 5.3 L7.4 5.7 L7.2 6.6 Q5.2 7.2 3.4 4.8 Z" fill="var(--icon-blue)"/></svg>
          <span>+49 69 4410 2716</span>
        </div>
        <div class="contact-line">
          <svg class="contact-icon" viewBox="0 0 10 10"><circle cx="5" cy="5" r="5" fill="var(--icon-blue)"/><rect x="2.6" y="3.6" width="4.8" height="3" rx="0.4" fill="#fff"/></svg>
          <span>+49 69 4410 2717</span>
        </div>
      </div>

      <span class="contact-divider"></span>

      <div class="contact-group online">
        <div class="contact-line">
          <svg class="contact-icon" viewBox="0 0 10 10"><circle cx="5" cy="5" r="5" fill="var(--icon-blue)"/><rect x="2.5" y="3.2" width="5" height="3.6" fill="#fff"/><path d="M2.5 3.2 L5 5.2 L7.5 3.2" fill="none" stroke="var(--icon-blue)" stroke-width="0.7"/></svg>
          <span>hello@harborlinemed.com</span>
        </div>
        <div class="contact-line">
          <svg class="contact-icon" viewBox="0 0 10 10"><circle cx="5" cy="5" r="4.5" fill="none" stroke="var(--icon-blue)" stroke-width="1"/><ellipse cx="5" cy="5" rx="2" ry="4.5" fill="none" stroke="var(--icon-blue)" stroke-width="0.8"/><line x1="0.5" y1="5" x2="9.5" y2="5" stroke="var(--icon-blue)" stroke-width="0.8"/></svg>
          <span>www.harborlinemed.com</span>
        </div>
      </div>

      <span class="contact-divider"></span>

      <address class="contact-group postal" style="font-style: normal;">
        <span>Lindenweg 12, 60311</span>
        <span>Frankfurt am Main</span>
      </address>
    </footer>
  </main>
</body>
</html>
```